Lead Generating Website Design

We are looking for a brand new design for our existing website.
The existing website is www.brivopartners.com
The website is aimed at businesses that would like to licence the courses from our school to sell themselves.
We want the menu to be the following:
* Home
* About us
* Our Courses
* LMS Platform
* Affiliate Program
* Contact Us
We want the colour scheme to use the following design guide:
https://folioshelf.net/stepsforward/docs/glide_and_wander_brand_guidelines
Like the idea of the circles and colours in the style guide for places. Want lots of white areas as well as coloured areas
An example of a nice looking site is : https://www.studyharbor.online/
MUST look good on mobile also
On the home page we want the following:
A large image with the text :
Over 450 courses written by highly qualified academics with real world experience.
The 'Join our thriving group of Affiliates - start your own online college!' section on the current website with the text and becoming an affiliate video
A section for 'see how our LMS works' with some text and a place for a video
A section for 'About Brivo Remote Learning' with the text Brivo Remote Learning has been providing distance education for over 40 years and have been the leader in online education for over 25 years.
Benefit from the resources and experience of one of the worlds leading course content providers.
Our highly qualified academic staff, HUGE resource library of up to date courses and cutting edge white label LMS enable our affiliates to stay well ahead of their competitors
A section for 'Free information pack' like the one on https://www.studyharbor.online/
Target Market(s)
Education providers looking to licence our courses to sell
Number of Pages Required
1 page
Look and feel

```html
<!DOCTYPE html>
<html lang="en">
<head>
<meta charset="utf-8">
<title>Brivo Remote Learning – Affiliate Program</title>
<link href="https://fonts.googleapis.com/css2?family=Cinzel:wght@500;600;700&family=Mulish:wght@400;500&family=Roboto+Condensed:wght@300;400&display=swap" rel="stylesheet">
<style>
:root{
  --navy:#0a4160;
  --gold:#e9b84a;
  --coral:#ef5b5a;
  --sun:#f3c15c;
  --ink:#2d3740;
  --white:#ffffff;
  --line:#f6b7b5;
}
*{box-sizing:border-box;margin:0;padding:0}
html,body{width:1200px;height:3400px;overflow:hidden;background:var(--white)}
body{position:relative;font-family:'Mulish',sans-serif;color:var(--ink)}
.abs{position:absolute}
.btn{position:absolute;background:var(--navy);color:var(--gold);font-family:'Cinzel',serif;font-weight:600;font-size:19px;display:flex;align-items:center;justify-content:center;letter-spacing:.5px;white-space:nowrap}

/* header */
.brand{position:absolute;left:142px;top:22px;width:222px}
.brand-name{font-family:'Cinzel',serif;font-size:15px;color:var(--navy);font-weight:500;letter-spacing:.3px;white-space:nowrap}
.brand-tag{margin-top:22px;background:var(--navy);color:var(--gold);font-family:'Cinzel',serif;font-weight:600;font-size:17px;text-align:center;padding:2px 0;letter-spacing:1px}
.contact-top{position:absolute;top:28px;display:flex;align-items:center;gap:12px;font-size:15px;color:var(--ink)}
.contact-top svg{width:30px;height:30px}
.main-nav{position:absolute;top:78px;left:475px;display:flex;gap:14px;font-family:'Cinzel',serif;font-size:15px;font-weight:500;color:var(--navy);letter-spacing:.3px}

/* hero */
.hero{position:absolute;left:0;top:112px;width:1200px;height:495px;background:linear-gradient(90deg,#e8e6e1 0%,#f1efea 45%,#d9d0c5 70%,#e9e7e3 100%)}
.hero-text{position:absolute;left:141px;top:134px;width:640px;font-family:'Roboto Condensed',sans-serif;font-weight:400}
.hero-text span{display:block;white-space:nowrap}
.hero-text h1{font-weight:400;font-size:28px;line-height:43px;color:var(--navy)}
.hero-text p{font-size:24px;line-height:34px;color:var(--coral);margin-top:2px}

/* lms */
.lms-band{position:absolute;left:0;top:607px;width:1200px;height:363px;background:var(--navy)}
.lms-band h2{position:absolute;top:82px;width:100%;text-align:center;font-family:'Cinzel',serif;color:var(--gold);font-size:31px;font-weight:600;letter-spacing:1px}
.lms-band p{position:absolute;top:142px;left:160px;width:880px;text-align:center;color:var(--white);font-size:13px;line-height:23px}
.video{position:absolute;left:275px;top:840px;width:650px;height:362px;background:#f6f6f6;border:3px solid #eaeaea}
.video-art{position:absolute;inset:0;background:linear-gradient(90deg,#f7f7f7 0%,#ededed 60%,#e2e6ea 100%)}
.video-bar{position:absolute;left:8px;right:4px;bottom:4px;height:22px;display:flex;gap:8px;align-items:center}
.video-bar .play-s{width:46px;height:24px;background:#222;display:flex;align-items:center;justify-content:center}
.video-bar .track{flex:1;height:20px;background:#2d2d2d}
.vid-side{position:absolute;right:4px;top:6px;display:flex;flex-direction:column;gap:6px}
.vid-side span{width:24px;height:24px;background:#222;border-radius:3px}

/* about */
.photo{position:absolute;background:linear-gradient(135deg,#c9d9cc,#e3ebe6 50%,#b8c4c7)}
.section-title{font-family:'Cinzel',serif;color:var(--navy);font-weight:600;letter-spacing:1px}
.about-copy{position:absolute;left:636px;top:1347px;width:440px}
.about-copy h2{font-size:30px;line-height:46px;white-space:nowrap}
.about-copy p{font-size:15px;line-height:25px;margin-top:4px}

/* info */
.info-left{position:absolute;left:140px;top:1870px;width:440px}
.info-left h2{font-size:29px;white-space:nowrap}
.info-left h3{font-weight:400;font-size:21px;margin-top:24px}
.info-left h4{font-weight:400;font-size:21px;margin-top:22px}
.info-left ul{margin:14px 0 0 22px;font-size:15px;line-height:31px}
.info-form{position:absolute;left:600px;top:1778px;width:600px;height:452px;background:var(--coral)}
.field{position:absolute;left:48px;width:385px;border-bottom:1.5px solid var(--line);display:flex;align-items:center;gap:14px;color:var(--white);font-size:12px;padding-bottom:10px}
.field svg{width:16px;height:16px}

/* different */
.diff-copy{position:absolute;left:641px;top:2330px;width:500px}
.diff-copy h2{font-size:29px;white-space:nowrap}
.diff-copy ul{margin:14px 0 0 18px;font-size:15px;line-height:25px}
.diff-copy p{font-size:21px;line-height:34px;margin-top:22px}
.diff-copy .hl{color:var(--coral)}

/* cta */
.cta{position:absolute;top:2760px;width:1200px;text-align:center}
.cta h2{font-size:30px}
.cta p{font-size:21px;line-height:34px;margin:8px auto 0;width:830px}

/* footer */
.footer{position:absolute;left:0;top:3015px;width:1200px;height:385px;background:var(--sun)}
.f-card{position:absolute;top:80px;width:214px;height:156px;border:1px solid #f7d38d;display:flex;flex-direction:column;align-items:center;justify-content:center;color:var(--navy)}
.f-card .lbl{font-family:'Cinzel',serif;font-size:16px;font-weight:600;margin-top:10px}
.f-card .val{font-size:14px;margin-top:2px}
.f-brand{position:absolute;left:474px;top:127px;width:248px;text-align:center}
.f-brand .brand-tag{margin-top:16px;font-size:18px}
.f-nav{position:absolute;top:282px;left:0;width:1200px;display:flex;justify-content:center;gap:34px;font-family:'Cinzel',serif;font-size:14px;font-weight:600;color:var(--navy)}
.f-rule{position:absolute;top:320px;left:145px;width:910px;border-top:1px solid #f7d38d}
.f-copy{position:absolute;top:342px;width:1200px;text-align:center;font-family:'Cinzel',serif;font-size:13px;color:var(--navy)}
</style>
</head>
<body>

<header>
  <div class="brand">
    <div class="brand-name">Brivo Remote Learning</div>
    <div class="brand-tag">AFFILIATE PROGRAM</div>
  </div>
  <div class="contact-top" style="left:698px">
    <svg viewBox="0 0 30 30"><circle cx="15" cy="15" r="14" fill="none" stroke="#0a4160" stroke-width="1.2"/><path d="M10.5 9.5l2.5-.5 1.3 3-1.5 1.2a7 7 0 0 0 3 3l1.2-1.5 3 1.3-.5 2.5c-4.5.5-9.5-4.5-9-9z" fill="none" stroke="#0a4160" stroke-width="1.2"/></svg>
    <span>555.014.2290</span>
  </div>
  <div class="contact-top" style="left:863px">
    <svg viewBox="0 0 30 30"><circle cx="15" cy="15" r="14" fill="none" stroke="#0a4160" stroke-width="1.2"/><rect x="9" y="11" width="12" height="9" fill="none" stroke="#0a4160" stroke-width="1.2"/><path d="M9 11l6 5 6-5" fill="none" stroke="#0a4160" stroke-width="1.2"/></svg>
    <span style="font-size:14px">hello@brivopartners.com</span>
  </div>
  <nav class="main-nav"><span>About us</span><span>Our Courses</span><span>LMS Platform</span><span>Affiliate Program</span><span>Contact Us</span></nav>
</header>

<section class="hero" role="img" aria-label="Smiling woman sitting cross-legged in a bright room working on a laptop">
  <div class="hero-text">
    <h1><span>Over 450 Courses Written By Highly Qualified</span><span>Academics With Real World Experience</span></h1>
    <p><span>The ‘Join Our Thriving Group Of Affiliates - Start</span><span>Your Own Online College!’</span></p>
  </div>
  <div class="btn" style="left:141px;top:305px;width:154px;height:42px">Learn More</div>
</section>

<section class="lms-band">
  <h2>See How Our Lms Works</h2>
  <p>lorem ipsum dolor sit amet, consectetuer adipiscing elit, sed diam nonummy nibh euismod tincidunt ut laoreet dolore magna aliquam erat volutpat. ut wisi enim ad minim veniam, quis nostrud exerci tation ullamcorper suscipit lobortis nisl ut aliquip ex ea commodo consequat. duis autem vel eum iriure dolor in hendrerit in vulputate velit.</p>
</section>
<div class="video">
  <div class="video-art" role="img" aria-label="Video still: illustrated agent working at a desk with a computer, titled Become an agent"></div>
  <div class="vid-side"><span></span><span></span><span></span></div>
  <svg class="abs" style="left:268px;top:136px" width="110" height="66" viewBox="0 0 110 66"><rect width="110" height="66" rx="6" fill="#ef4a45"/><path d="M46 20l22 13-22 13z" fill="#fff"/></svg>
  <div class="video-bar">
    <div class="play-s"><svg width="12" height="12" viewBox="0 0 12 12"><path d="M2 1l9 5-9 5z" fill="#fff"/></svg></div>
    <div class="track"></div>
  </div>
</div>

<div class="photo" style="left:0;top:1298px;width:600px;height:480px" role="img" aria-label="Woman in striped shirt smiling while typing on a laptop by a window"></div>
<section class="about-copy">
  <h2 class="section-title">About<br>Brivo Remote Learning</h2>
  <p>Brivo Remote Learning has been providing distance education for over 40 years and have been the leader in online education for over 25 years.</p>
  <p>Benefit from the resources and experience of one of the worlds leading course content providers.</p>
  <p>Our highly qualified academic staff, HUGE resource library of up to date courses &amp; cutting edge white label LMS enable our affiliates to stay well ahead of their competitors.</p>
</section>
<div class="btn" style="left:639px;top:1666px;width:216px;height:42px">Contact Us Today</div>

<section class="info-left">
  <h2 class="section-title">Free Information Pack</h2>
  <h3>Get Free Access To Our Info Packs</h3>
  <h4>What’s in the info packs?</h4>
  <ul>
    <li>Full list of available course learning resources</li>
    <li>Complete how it works guide</li>
    <li>Latest offers and special promos</li>
    <li>Frequently asked questions</li>
  </ul>
</section>
<form class="info-form">
  <div class="field" style="top:90px"><svg viewBox="0 0 16 16"><circle cx="8" cy="5" r="3.2" fill="none" stroke="#fff"/><path d="M2 15c0-4 12-4 12 0" fill="none" stroke="#fff"/></svg>First Name</div>
  <div class="field" style="top:140px"><svg viewBox="0 0 16 16"><rect x="1.5" y="3.5" width="13" height="9" fill="none" stroke="#fff"/><path d="M1.5 3.5l6.5 5 6.5-5" fill="none" stroke="#fff"/></svg>Email</div>
  <div class="field" style="top:192px"><svg viewBox="0 0 16 16"><rect x="1.5" y="3.5" width="10" height="10" fill="none" stroke="#fff"/><path d="M7 9l7-7" stroke="#fff"/></svg>Send me an info pack &amp; course list information</div>
  <div class="field" style="top:242px;height:56px;align-items:flex-start"><svg viewBox="0 0 16 16"><circle cx="8" cy="7" r="6" fill="none" stroke="#fff"/><path d="M5 7h6M5 9h4" stroke="#fff"/></svg>Message</div>
  <div class="btn" style="left:48px;top:312px;width:118px;height:42px">Submit</div>
</form>

<div class="photo" style="left:0;top:2230px;width:600px;height:450px;background:linear-gradient(135deg,#a8b59a,#e9e1d3 50%,#c99a4a)" role="img" aria-label="Woman relaxing in a mustard armchair with a mug beside a laptop on a stand"></div>
<section class="diff-copy">
  <h2 class="section-title">How are we different?</h2>
  <ul>
    <li>No Set Up Costs</li>
    <li>No Fixed Costs</li>
    <li>Pay For Content As You Use It</li>
    <li>True Plug And Play Solution</li>
  </ul>
  <p>Speak to our team today on <span class="hl">555.014.2290</span><br>or email hello@brivopartners.com</p>
</section>

<section class="cta">
  <h2 class="section-title">Interested in becoming an affiliate?</h2>
  <p>Contact us now to discuss how we can work together to launch your own Distance Education Business...</p>
</section>
<div class="btn" style="left:492px;top:2883px;width:216px;height:41px">Contact Us Today</div>
<div class="abs" style="left:545px;top:2966px;width:118px;height:42px;background:var(--navy)"></div>

<footer class="footer">
  <div class="f-card" style="left:189px">
    <svg width="44" height="42" viewBox="0 0 44 42"><path d="M4 16L22 3l18 13v23H4z" fill="none" stroke="#0a4160" stroke-width="2"/><rect x="10" y="9" width="24" height="16" fill="none" stroke="#0a4160" stroke-width="2"/><path d="M4 16l18 13 18-13M4 39l14-11M40 39L26 28" fill="none" stroke="#0a4160" stroke-width="2"/></svg>
    <div class="lbl">Email</div>
    <div class="val">hello@brivopartners.com</div>
  </div>
  <div class="f-brand">
    <div class="brand-name" style="font-size:16px">Brivo Remote Learning</div>
    <div class="brand-tag">AFFILIATE PROGRAM</div>
  </div>
  <div class="f-card" style="left:797px">
    <svg width="42" height="42" viewBox="0 0 42 42"><path d="M8 5l7-1 3 8-4 3a18 18 0 0 0 13 13l3-4 8 3-1 7C22 35 7 20 8 5z" fill="none" stroke="#0a4160" stroke-width="2"/><path d="M25 5a12 12 0 0 1 12 12M25 11a6 6 0 0 1 6 6" fill="none" stroke="#0a4160" stroke-width="2"/></svg>
    <div class="lbl">Phone</div>
    <div class="val">555.014.2290</div>
  </div>
  <nav class="f-nav"><span>About us</span><span>Our Courses</span><span>LMS Platform</span><span>Affiliate Program</span><span>Contact Us</span></nav>
  <div class="f-rule"></div>
  <div class="f-copy">© 2021 <b>Brivo Remote Learning.</b> All Rights Reserved.</div>
</footer>

</body>
</html>
```